FotoVELTA buisnesscard

Hey :) I need a modern buisnesscard for my company FotoVELTA
It most have:
Dagligleder og Fotograf: Henrik Torvald Bjelland

Mob: +4791642058
Epost: post@fotovelta.no
Adresse: Bakkestien22, 6030 Langevåg

Facbook and instagram logo with text FotoVELTA

FotoVELTA logo

It Company

```html
<!DOCTYPE html>
<html lang="no">
<head>
<meta charset="utf-8">
<title>FotoVELTA – visittkort</title>
<link rel="stylesheet" href="https://fonts.googleapis.com/css2?family=Lato:wght@400;700;900&display=swap">
<style>
  :root {
    --backdrop: #3a3a3a;
    --ink: #000000;
    --paper: #ffffff;
    --brand-grey: #aeadad;
    --text-dark: #111111;
    --icon-grey: #9a9a9a;
  }
  * { box-sizing: border-box; margin: 0; padding: 0; }
  html, body {
    width: 1200px; height: 900px; overflow: hidden;
    background: var(--backdrop);
    font-family: "Lato", sans-serif;
  }
  .stage { position: relative; width: 1200px; height: 900px; }
  .card {
    position: absolute; left: 260px; width: 680px; height: 388px;
    overflow: hidden; box-shadow: 0 10px 30px rgba(0,0,0,.45);
  }
  .card--back { top: 46px; background: var(--ink); display: flex; align-items: center; justify-content: center; }
  .card--front { top: 466px; background: var(--paper); }
  .brand-name {
    font-family: "Lato", sans-serif; font-weight: 900;
    color: var(--brand-grey); letter-spacing: 1px; line-height: 1;
    white-space: nowrap;
  }
  .card--back .brand-name { font-size: 72px; }
  .front__edge { position: absolute; left: 0; top: 0; width: 36px; height: 100%; background: var(--paper); }
  .front__panel {
    position: absolute; left: 36px; top: 0; width: 320px; height: 100%;
    background: var(--ink); color: var(--paper); padding: 30px 28px;
  }
  .holder-name { font-weight: 700; font-size: 21px; white-space: nowrap; }
  .holder-role { font-weight: 400; font-size: 17px; margin-top: 4px; }
  .front__info { position: absolute; left: 356px; top: 0; right: 0; height: 100%; }
  .front__info .brand-name { position: absolute; top: 92px; left: 0; right: 0; text-align: center; font-size: 54px; }
  .address { position: absolute; left: 70px; top: 190px; font-size: 20px; color: var(--text-dark); line-height: 1.2; }
  .contact-list { position: absolute; left: 40px; top: 252px; list-style: none; font-size: 20px; color: var(--text-dark); }
  .contact-list li { display: flex; align-items: center; height: 26px; white-space: nowrap; }
  .contact-icon { width: 18px; height: 18px; margin-right: 12px; flex: none; }
  .contact-mark { width: 16px; height: 16px; margin: 0 13px 0 1px; background: var(--icon-grey); border-radius: 3px; flex: none; }
</style>
</head>
<body>
<main class="stage">
  <section class="card card--back" aria-label="Visittkort, bakside">
    <span class="brand-name">FotoVELTA</span>
  </section>

  <section class="card card--front" aria-label="Visittkort, forside">
    <div class="front__edge"></div>
    <div class="front__panel">
      <p class="holder-name">Henrik Torvald Bjelland</p>
      <p class="holder-role">Dagligleder og Fotograf</p>
    </div>
    <div class="front__info">
      <span class="brand-name">FotoVELTA</span>
      <p class="address">Bakkestien 22<br>6099 Fjordvik</p>
      <ul class="contact-list">
        <li>
          <svg class="contact-icon" viewBox="0 0 18 18" aria-hidden="true">
            <rect x="4" y="1" width="10" height="16" rx="2" fill="none" stroke="var(--icon-grey)" stroke-width="1.8"/>
            <circle cx="9" cy="14" r="1" fill="var(--icon-grey)"/>
          </svg>
          +4791642058
        </li>
        <li>
          <svg class="contact-icon" viewBox="0 0 18 18" aria-hidden="true">
            <rect x="1" y="4" width="16" height="11" fill="none" stroke="var(--icon-grey)" stroke-width="1.6"/>
            <path d="M1 4 L9 10 L17 4" fill="none" stroke="var(--icon-grey)" stroke-width="1.6"/>
          </svg>
          post@fotovelta.no
        </li>
        <li><span class="contact-mark"></span>FotoVELTA</li>
        <li><span class="contact-mark"></span>FotoVELTA</li>
      </ul>
    </div>
  </section>
</main>
</body>
</html>
```